Premium CBD/Hemp company needs packaging and label design

Verdant Halcyon Labs, a premium CBD/Hemp company based in Scottsdale, Arizona is in need of a packaging and label design. We are launching with our flagship product which will be a 30 count capsule and will come in three functions: Pain Relief, Anxiety Support, and Sleep Support. For the purpose of this contest, please design packaging and label for our Anxiety Support product. Our products are physician formulated and all natural. Our main ingredient is CBD/Hemp and is complemented by specific herbs that synergistically work together to give the customer the most effective and desired result. We would like our branding to have a pharmaceutical look and feel with a focus on trust and transparency. We have uploaded our company logo that is to be used on both the packaging and label. We have also uploaded an executed branding questionnaire that will guide you to exactly what we are seeking to achieve as to the look and feel of our brand. Please feel free to contact us with any questions that you may have. The winner of this contest will have the opportunity to work with us on future projects as we will need packaging and label design for our entire Verdant Halcyon Labs product line.

Target Market(s)

See attached branding questionnaire

Industry/Entity Type

Health And Wellness

Font styles to use
Sans Serif

Colors

Designer to choose colors to be used in the design.

Requirements
Must have
• See attached branding questionnaire; Please superimpose labels onto a cobalt blue capsule bottle (see attached)
• >>UPON REVIEW of the FIRST 8 designs, we really like the silver, mildly metallic label background in DESIGN # 21300528, we do not want metalic lettering as that would not look very "Pharmaceutical"
• >>We are in search of a look that is a bit more "Pharmaceutical" than a look that would be more commonly found in a Supplement Store
Nice to have
• "See attached branding questionnaire
Should not have
• See attached branding questionnaire; NO marijuana or cannabis plant on the packaging or label

```html
<!DOCTYPE html>
<html lang="en">
<head>
<meta charset="utf-8">
<title>Verdant Halcyon Labs – Full Spectrum Hemp Extract, Anxiety Support</title>
<link href="https://fonts.googleapis.com/css2?family=Montserrat:wght@800&family=Roboto+Condensed:wght@400;500;700&display=swap" rel="stylesheet">
<style>
  :root {
    --stage: #0b0b0b;
    --white: #ffffff;
    --paper: #f6f6f6;
    --silver-light: #eeeeee;
    --silver-mid: #cfcfcf;
    --silver-dark: #b9b9b9;
    --green: #35a050;
    --green-deep: #1f7d3b;
    --green-dark: #17692f;
    --navy: #28337a;
    --blue-band: #3b4fa3;
    --rule: #8c8c8c;
  }
  * { box-sizing: border-box; margin: 0; padding: 0; }
  html, body { width: 1200px; height: 1200px; overflow: hidden; background: var(--stage); }
  body { font-family: "Roboto Condensed", Arial, sans-serif; }

  .carton { position: absolute; left: 180px; top: 100px; width: 840px; height: 1000px; display: flex; }

  /* Front label panel */
  .front-panel {
    position: relative; width: 420px; height: 1000px; overflow: hidden;
    background: linear-gradient(to bottom, var(--white) 0%, var(--paper) 58%, var(--silver-light) 62%, var(--silver-mid) 78%, var(--silver-light) 90%, var(--silver-dark) 100%);
    text-align: center; color: var(--navy);
  }
  .brand { position: absolute; top: 120px; left: 0; width: 100%; display: flex; justify-content: center; align-items: center; gap: 12px; }
  .brand-dot { width: 34px; height: 34px; border-radius: 50%; border: 3px solid var(--green); flex: none; }
  .brand-name { font-weight: 500; font-size: 26px; line-height: 1.05; letter-spacing: 1px; text-transform: uppercase; color: var(--navy); text-align: left; }

  .spectrum-tag {
    position: absolute; top: 448px; left: 50%; transform: translateX(-50%);
    border: 3px solid var(--blue-band); padding: 3px 12px;
    font-weight: 700; font-size: 22px; color: var(--navy); white-space: nowrap;
  }
  .product-name { position: absolute; top: 490px; left: 0; width: 100%; color: var(--green); font-weight: inherit; }
  .product-name .hemp { display: block; font-family: "Montserrat", Arial, sans-serif; font-weight: 800; font-size: 88px; line-height: 1; letter-spacing: 1px; }
  .product-name .extract { display: block; font-weight: 400; font-size: 52px; line-height: 1; letter-spacing: 1px; margin-top: 4px; }

  .natural-band { position: absolute; top: 640px; left: 0; width: 420px; height: 60px; }
  .natural-band svg { display: block; }
  .natural-band text { font-family: "Roboto Condensed", Arial, sans-serif; font-weight: 700; font-size: 26px; fill: var(--white); letter-spacing: .5px; }

  .function { position: absolute; top: 808px; left: 50%; transform: translateX(-50%); width: 250px; }
  .function hr { border: 0; border-top: 2px solid var(--rule); }
  .function hr + hr { margin-top: 3px; }
  .function p { font-weight: 700; font-size: 24px; color: var(--navy); padding: 14px 0; }

  .facts { position: absolute; top: 928px; left: 50%; transform: translateX(-50%); text-align: center; }
  .facts .kind { font-weight: 700; font-size: 12px; color: var(--navy); margin-bottom: 6px; }
  .facts .pill { display: flex; border: 2px solid var(--navy); border-radius: 12px; overflow: hidden; width: 170px; height: 26px; }
  .facts .pill .count { background: var(--navy); color: var(--white); font-size: 11px; font-weight: 700; width: 92px; line-height: 22px; }
  .facts .pill .dose { color: var(--navy); font-size: 15px; font-weight: 700; flex: 1; line-height: 22px; }

  /* Side panel */
  .side-panel {
    position: relative; width: 420px; height: 1000px;
    background: linear-gradient(to right, var(--green-dark) 0%, var(--green-deep) 45%, var(--green) 100%);
  }
  .side-panel .brand { top: 420px; }
  .side-panel .brand-dot { border-color: var(--white); }
  .side-panel .brand-name { color: var(--white); }
</style>
</head>
<body>
  <main class="carton">
    <section class="front-panel">
      <div class="brand">
        <span class="brand-dot"></span>
        <span class="brand-name">Verdant Halcyon<br>Labs</span>
      </div>

      <div class="spectrum-tag">FULL SPECTRUM</div>
      <h1 class="product-name">
        <span class="hemp">HEMP</span>
        <span class="extract">EXTRACT</span>
      </h1>

      <div class="natural-band">
        <svg width="420" height="60" viewBox="0 0 420 60">
          <rect x="0" y="12" width="420" height="10" fill="#3b4fa3"/>
          <rect x="0" y="22" width="420" height="6" fill="#35a050"/>
          <polygon points="70,6 350,6 330,54 90,54" fill="#35a050"/>
          <text x="210" y="40" text-anchor="middle">ALL NATURAL</text>
        </svg>
      </div>

      <div class="function">
        <hr><hr>
        <p>ANXIETY SUPPORT</p>
        <hr><hr>
      </div>

      <div class="facts">
        <div class="kind">DIETARY SUPPLEMENT</div>
        <div class="pill"><span class="count">30 CAPSULES</span><span class="dose">25MG</span></div>
      </div>
    </section>

    <section class="side-panel">
      <div class="brand">
        <span class="brand-dot"></span>
        <span class="brand-name">Verdant Halcyon<br>Labs</span>
      </div>
    </section>
  </main>
</body>
</html>
```